Brisket Electrical Business Card Design

A Registered Electrical Contractor with +21 years experience backed with advanced electrical and electronics education. The design should appeal to the industrial, commercial and domestic electrical industry. Final design should communicate prompt, diverse, professional service.
Updates

The Business Name is "Brisket Electrical" not brisket Electrical South Eastern Suburbs

Reason: I have committed payment, removed colour limitations and asked for images to be added so designers can have more freedom to capture the audience with the WOW factor. So go for it and show me what you got. GOOD LUCK EVERYONE

Target Market(s)

Target Industrial business sector, domestic faults and repairs.
We cover all electrical faults, power, lighting, installation, control wiring, machines, process lines, appliances, maintenance, compliance testing, overhead cranes, switchboards and more.

Industry/Entity Type

Electronics

Contact Information for Business Card

Brisket Electrical
South Eastern Suburbs
Melbourne, Victoria 3976
0432 519 284
brisketelectrical@mailpost.example
ABN: 48 206 953 172
REC: 37509

Requirements
Must have
• 1 - "REC: 37509" should be at the top righthand corner.
2 - Trade picture to reflect wow factor. e.g Lighning, electrician.
3 - List format:( I will ask you to edit as required if design looks too cluttered)
Industrial, Commercial, Domestic, Manufacturing, Installation, Faults, Maintenance,
Commissioning, Compliance Testing, HV Equipment, Generators, Pumps, Overhead Cranes, Power, Lighting, Appliances, Leads, Process Lines, Control Wiring, Main Control Cubicles, Switchboards, Motor Control, VSD, PLC, Electronics, …
Nice to have
• The letters B and E as a combined shape to be used as a logo
Should not have
• "since 21 Year"

```html
<!DOCTYPE html>
<html lang="en">
<head>
<meta charset="utf-8">
<title>Brisket Electrical – Business Card</title>
<link rel="stylesheet" href="https://fonts.googleapis.com/css2?family=Open+Sans:wght@400;600;700&display=swap">
<style>
  :root {
    --page-bg: #e9e7e4;
    --card-black: #0b0b0d;
    --card-charcoal: #1c1c20;
    --electric-cyan: #2aa8df;
    --cyan-deep: #1b86bd;
    --navy-ink: #0b2a44;
    --storm-violet: #2b2f95;
    --storm-glow: #bfcaff;
    --text-white: #f2f4f6;
  }
  * { box-sizing: border-box; margin: 0; padding: 0; }
  html, body {
    width: 1200px; height: 1023px; overflow: hidden;
    background: var(--page-bg);
    font-family: "Open Sans", Arial, sans-serif;
  }
  .business-card {
    position: absolute; left: 100px; top: 206px;
    width: 1000px; height: 611px;
    border-radius: 26px; overflow: hidden;
    background: linear-gradient(160deg, var(--card-charcoal) 0%, var(--card-black) 60%);
    box-shadow: 0 18px 40px rgba(0,0,0,.35);
  }
  .storm-photo {
    position: absolute; left: 330px; top: 0; width: 670px; height: 330px;
    background:
      radial-gradient(ellipse 40% 35% at 38% 18%, var(--storm-glow) 0%, rgba(120,135,240,.75) 18%, transparent 60%),
      radial-gradient(ellipse 70% 80% at 45% 30%, var(--storm-violet) 0%, rgba(22,24,90,.85) 45%, transparent 80%);
  }
  .accent-band {
    position: absolute; left: 0; top: 330px; width: 100%; height: 44px;
    background: linear-gradient(180deg, #43b9ec 0%, var(--electric-cyan) 50%, var(--cyan-deep) 100%);
  }
  .licence-number {
    position: absolute; right: 40px; top: 8px;
    font-size: 22px; font-weight: 600; letter-spacing: 1px;
    color: var(--navy-ink);
  }
  .brand {
    position: absolute; left: 60px; top: 150px;
    display: flex; align-items: center; gap: 26px;
  }
  .brand-dot {
    width: 120px; height: 120px; border-radius: 50%;
    background: var(--electric-cyan);
  }
  .brand-name {
    font-size: 58px; font-weight: 600; line-height: 1.02;
    letter-spacing: 4px; text-transform: uppercase;
    color: var(--text-white);
  }
  .contact {
    position: absolute; left: 100px; top: 405px;
    color: var(--text-white);
  }
  .person-name {
    font-size: 38px; font-weight: 700; letter-spacing: 1px;
    color: var(--electric-cyan); text-transform: uppercase; line-height: 1.1;
  }
  .person-role { font-size: 20px; margin: 2px 0 22px; }
  .contact-line {
    display: flex; align-items: center; gap: 14px;
    font-size: 25px; line-height: 1; margin-bottom: 16px;
  }
  .contact-icon { width: 26px; height: 26px; flex: none; }
  .business-details {
    position: absolute; right: 60px; top: 410px;
    text-align: right; font-size: 25px; line-height: 1.35;
    color: var(--electric-cyan); text-transform: uppercase;
  }
  .business-details .label { font-weight: 700; }
  .business-details .number { color: var(--text-white); }
</style>
</head>
<body>
  <article class="business-card">
    <div class="storm-photo" role="img" aria-label="Photograph of blue lightning bolts against a dark night sky"></div>

    <div class="brand">
      <div class="brand-dot"></div>
      <div class="brand-name">Brisket<br>Electrical</div>
    </div>

    <div class="accent-band">
      <span class="licence-number">REC: 37509</span>
    </div>

    <section class="contact">
      <h1 class="person-name">Dale Morrow</h1>
      <p class="person-role">Director</p>
      <p class="contact-line">
        <svg class="contact-icon" viewBox="0 0 26 26" aria-hidden="true">
          <rect width="26" height="26" rx="4" fill="var(--text-white)"/>
          <path d="M8 6c1-1 2 0 3 2s0 2-1 3c1 2 2 3 4 4 1-1 1-2 3-1s3 2 2 3c-1 2-3 3-6 1-3-2-5-4-6-7-1-2 0-4 1-5z" fill="var(--card-black)"/>
        </svg>
        0432 519 284
      </p>
      <p class="contact-line">
        <svg class="contact-icon" viewBox="0 0 26 26" aria-hidden="true">
          <rect width="26" height="26" rx="4" fill="var(--text-white)"/>
          <rect x="5" y="8" width="16" height="11" rx="1" fill="var(--card-black)"/>
          <path d="M5.5 8.5 13 14l7.5-5.5" stroke="var(--text-white)" stroke-width="1.5" fill="none"/>
        </svg>
        brisketelectrical@mailpost.example
      </p>
    </section>

    <section class="business-details">
      <p><span class="label">ABN:</span> <span class="number">48 206 953 172</span></p>
      <p>South Eastern Suburbs</p>
    </section>
  </article>
</body>
</html>
```